Label design/Graphic design required to brand wall paints

Would like to design a paint drum label/graphic to brand paint drums. The product is wall paints which come in plastic containers. (Refer attached pics). I have also attached the logo font. The one in the pictures are a bit too plan - need some color and creativity - not something too jazzy. You can change the icons if you wish to for the Low VOC, Washable & Eco Friendly - or keep the same. Need to incorporate the drum size "20 L" or "20 Ltr." at the bottom of the label.Rest of the matter to be incorporated is as per the content in the sample labels provided. Size of the label can be 230 x 230mm W X H.

Target Market(s)

Buildings Houses

Industry/Entity Type

Painting And Decorating

Colors

Designer to choose colors to be used in the design.

Requirements
Must have
• The content on the label samples given. Must maintain the logo font.
Nice to have
• A little more color -not jazzy. Can try giving color accents to the font if it helps.
Should not have
• Should not be cluttered.

```html
<!DOCTYPE html>
<html lang="en">
<head>
<meta charset="utf-8">
<title>Verano – Drum Labels</title>
<link href="https://fonts.googleapis.com/css2?family=Josefin+Sans:wght@300&family=Open+Sans:wght@400&display=swap" rel="stylesheet">
<style>
  :root {
    --page: #ffffff;
    --label-bg: #ebecec;
    --ink: #111111;
    --paper: #f7f7f7;
    --pink: #ff4f86;
    --coral: #ff7a6b;
    --orange: #ffb14e;
    --peach: #f8c6a4;
    --blush: #f9d3d3;
  }
  html, body {
    margin: 0;
    width: 1200px;
    height: 810px;
    overflow: hidden;
    background: var(--page);
  }
  .sheet {
    width: 1200px;
    height: 810px;
    display: flex;
    align-items: center;
    justify-content: center;
    gap: 80px;
  }
  .label {
    width: 460px;
    height: 460px;
    border-radius: 12px;
    overflow: hidden;
    box-shadow: 0 4px 14px rgba(0,0,0,0.12);
  }
  .label svg { display: block; width: 100%; height: 100%; }
  .brand-name { font-family: "Josefin Sans", sans-serif; font-weight: 300; font-size: 66px; }
  .tagline { font-family: "Josefin Sans", sans-serif; font-weight: 300; font-size: 19px; }
  .feature-name { font-family: "Open Sans", sans-serif; font-size: 9.5px; fill: #333; }
  .volume { font-family: "Open Sans", sans-serif; font-size: 20px; fill: #fff; }
</style>
</head>
<body>
<main class="sheet">

  <section class="label label--light">
    <svg viewBox="0 0 415 415" xmlns="http://www.w3.org/2000/svg">
      <defs>
        <radialGradient id="glowA" cx="0.3" cy="0.3" r="0.8">
          <stop offset="0" stop-color="var(--pink)"/>
          <stop offset="0.55" stop-color="var(--coral)"/>
          <stop offset="1" stop-color="var(--orange)"/>
        </radialGradient>
        <linearGradient id="dropA" x1="0" y1="0" x2="0" y2="1">
          <stop offset="0" stop-color="var(--orange)"/>
          <stop offset="1" stop-color="var(--pink)"/>
        </linearGradient>
      </defs>
      <rect class="label-bg" width="415" height="415" fill="var(--label-bg)"/>
      <circle class="colour-glow" cx="70" cy="420" r="200" fill="url(#glowA)" opacity="0.9"/>
      <rect class="base-band" x="0" y="382" width="415" height="33" fill="var(--orange)" opacity="0.85"/>
      <rect class="feature-strip" x="0" y="313" width="415" height="16" fill="var(--blush)" opacity="0.8"/>

      <g class="brand-block">
        <rect x="60" y="40" width="295" height="150" fill="var(--paper)"/>
        <line x1="61" y1="40" x2="61" y2="222" stroke="var(--ink)" stroke-width="1.6"/>
        <text class="brand-name" x="82" y="140" fill="var(--ink)" textLength="252" lengthAdjust="spacingAndGlyphs">VERANO</text>
        <rect x="60" y="190" width="295" height="32" fill="var(--ink)"/>
        <text class="tagline" x="82" y="213" fill="#fff" textLength="252" lengthAdjust="spacingAndGlyphs">PAINT AND PRIMER</text>
      </g>

      <g class="features">
        <g transform="translate(130,282)">
          <rect x="-16" y="-16" width="32" height="32" rx="6" transform="rotate(45)" fill="#fff" stroke="var(--coral)" stroke-width="1.5"/>
          <path d="M-9,-2 q4,-5 9,0 t9,0 M-9,4 q4,-5 9,0 t9,0" fill="none" stroke="var(--ink)" stroke-width="1.3"/>
          <text class="feature-name" x="0" y="42" text-anchor="middle">WASHABLE</text>
        </g>
        <g transform="translate(202,282)">
          <rect x="-16" y="-16" width="32" height="32" rx="6" transform="rotate(45)" fill="#fff" stroke="var(--coral)" stroke-width="1.5"/>
          <path d="M0,-11 C9,-4 9,6 0,10 C-9,6 -9,-4 0,-11 Z M0,-8 V14" fill="none" stroke="var(--ink)" stroke-width="1.2"/>
          <text class="feature-name" x="0" y="42" text-anchor="middle">LOW VOC</text>
        </g>
        <g transform="translate(273,282)">
          <rect x="-16" y="-16" width="32" height="32" rx="6" transform="rotate(45)" fill="#fff" stroke="var(--coral)" stroke-width="1.5"/>
          <path d="M-3,-9 L3,-9 L7,-2 M9,3 L6,9 L-2,9 M-7,7 L-10,1 L-6,-5" fill="none" stroke="var(--ink)" stroke-width="1.3"/>
          <path d="M5,-4 L8,0 L9,-5 Z M-4,11 L-1,7 L-1,12 Z M-8,-3 L-3,-4 L-6,-8 Z" fill="var(--ink)"/>
          <text class="feature-name" x="0" y="42" text-anchor="middle">ECO FRIENDLY</text>
        </g>
      </g>

      <g class="volume-drop">
        <path d="M359,280 C370,298 388,318 388,340 A29,29 0 0 1 330,340 C330,318 348,298 359,280 Z" fill="url(#dropA)"/>
        <text class="volume" x="359" y="350" text-anchor="middle">20 L</text>
      </g>
    </svg>
  </section>

  <section class="label label--dark">
    <svg viewBox="0 0 415 415" xmlns="http://www.w3.org/2000/svg">
      <defs>
        <radialGradient id="glowB" cx="0.3" cy="0.3" r="0.8">
          <stop offset="0" stop-color="var(--pink)"/>
          <stop offset="0.55" stop-color="var(--coral)"/>
          <stop offset="1" stop-color="var(--orange)"/>
        </radialGradient>
        <linearGradient id="dropB" x1="0" y1="0" x2="0" y2="1">
          <stop offset="0" stop-color="var(--orange)"/>
          <stop offset="1" stop-color="var(--pink)"/>
        </linearGradient>
      </defs>
      <rect class="label-bg" width="415" height="415" fill="var(--label-bg)"/>
      <circle class="colour-glow" cx="70" cy="420" r="200" fill="url(#glowB)" opacity="0.9"/>
      <rect class="base-band" x="0" y="382" width="415" height="33" fill="var(--orange)" opacity="0.85"/>
      <rect class="feature-strip" x="0" y="313" width="415" height="16" fill="var(--blush)" opacity="0.8"/>

      <g class="brand-block">
        <rect x="60" y="40" width="295" height="150" fill="var(--ink)"/>
        <text class="brand-name" x="82" y="140" fill="#fff" textLength="252" lengthAdjust="spacingAndGlyphs">VERANO</text>
        <rect x="60" y="190" width="295" height="32" fill="var(--peach)"/>
        <text class="tagline" x="82" y="213" fill="#222" textLength="252" lengthAdjust="spacingAndGlyphs">PAINT AND PRIMER</text>
      </g>

      <g class="features">
        <g transform="translate(130,282)">
          <rect x="-16" y="-16" width="32" height="32" rx="6" transform="rotate(45)" fill="#fff" stroke="var(--coral)" stroke-width="1.5"/>
          <path d="M-9,-2 q4,-5 9,0 t9,0 M-9,4 q4,-5 9,0 t9,0" fill="none" stroke="var(--ink)" stroke-width="1.3"/>
          <text class="feature-name" x="0" y="42" text-anchor="middle">WASHABLE</text>
        </g>
        <g transform="translate(202,282)">
          <rect x="-16" y="-16" width="32" height="32" rx="6" transform="rotate(45)" fill="#fff" stroke="var(--coral)" stroke-width="1.5"/>
          <path d="M0,-11 C9,-4 9,6 0,10 C-9,6 -9,-4 0,-11 Z M0,-8 V14" fill="none" stroke="var(--ink)" stroke-width="1.2"/>
          <text class="feature-name" x="0" y="42" text-anchor="middle">LOW VOC</text>
        </g>
        <g transform="translate(273,282)">
          <rect x="-16" y="-16" width="32" height="32" rx="6" transform="rotate(45)" fill="#fff" stroke="var(--coral)" stroke-width="1.5"/>
          <path d="M-3,-9 L3,-9 L7,-2 M9,3 L6,9 L-2,9 M-7,7 L-10,1 L-6,-5" fill="none" stroke="var(--ink)" stroke-width="1.3"/>
          <path d="M5,-4 L8,0 L9,-5 Z M-4,11 L-1,7 L-1,12 Z M-8,-3 L-3,-4 L-6,-8 Z" fill="var(--ink)"/>
          <text class="feature-name" x="0" y="42" text-anchor="middle">ECO FRIENDLY</text>
        </g>
      </g>

      <g class="volume-drop">
        <path d="M359,280 C370,298 388,318 388,340 A29,29 0 0 1 330,340 C330,318 348,298 359,280 Z" fill="url(#dropB)"/>
        <text class="volume" x="359" y="350" text-anchor="middle">20 L</text>
      </g>
    </svg>
  </section>

</main>
</body>
</html>
```